Exhibition Print

Need to have a few video meetings and work scope
we have approx 20 panels that need to tell a story of our business
I have updated a story board'
Our main company is:
trelvon.com.au fibre to the home technologies for new or greenfield retirement estates and ethernet over copper for existing retirement estates

We will pay for the extra meetings on top

so the design needs approx 20 panels 2.4m HEIGHT x 1m WIDE
so we will work out the correct way to price this together

Target Market(s)

retirement communiites

Industry/Entity Type

retirement and communication technologies

Requirements
Nice to have
• i have attached a story board

```html
<!DOCTYPE html>
<html lang="en">
<head>
<meta charset="utf-8">
<title>Trelvon Health – Exhibition Panels</title>
<link href="https://fonts.googleapis.com/css2?family=Montserrat:wght@400;600;900&display=swap" rel="stylesheet">
<style>
:root{
  --page:#ffffff;
  --frame:#c9c9c9;
  --ink-blue:#0b4496;
  --band-blue:#064a9b;
  --band-text:#ffffff;
  --head-light:#f4f4f4;
  --head-mid:#d6d6d6;
  --rule-gold:#d8b25a;
}
*{box-sizing:border-box;margin:0;padding:0}
html,body{width:1200px;height:2287px;overflow:hidden;background:var(--page)}
.canvas{position:relative;width:1200px;height:2287px;border:1px solid var(--frame);background:var(--page)}
.wall{position:absolute;left:55px;top:50px;width:1102px;display:grid;grid-template-rows:repeat(4,530px);row-gap:23px}
.row{display:grid;grid-template-columns:repeat(5,minmax(0,1fr));height:530px}
.panel{display:flex;flex-direction:column;height:530px;min-width:0}
.panel-head{position:relative;height:123px;display:flex;align-items:center;justify-content:center;text-align:center;overflow:hidden;
  background:
    linear-gradient(115deg,transparent 0 40%,rgba(255,255,255,.55) 40% 55%,transparent 55%),
    linear-gradient(65deg,transparent 0 58%,rgba(0,0,0,.04) 58% 72%,transparent 72%),
    linear-gradient(135deg,var(--head-mid) 0%,var(--head-light) 30%,#ffffff 50%,var(--head-light) 70%,var(--head-mid) 100%)}
.panel+.panel .panel-head::before{content:"";position:absolute;left:0;top:14px;bottom:14px;width:1px;background:var(--rule-gold)}
.panel-title{font-family:"Montserrat",sans-serif;font-weight:900;color:var(--ink-blue);font-size:20px;line-height:23px;text-transform:uppercase;letter-spacing:.1px;padding:0 4px}
.panel-band{height:73px;background:var(--band-blue);display:flex;align-items:center;justify-content:center;text-align:center;padding:0 10px}
.panel-copy{font-family:"Montserrat",sans-serif;font-weight:400;color:var(--band-text);font-size:9px;line-height:12px}
.panel-copy b{font-weight:600}
.panel-photo{position:relative;flex:1;height:334px}
.panel-photo::after{content:"";position:absolute;inset:0;background:radial-gradient(ellipse at 50% 45%,transparent 55%,rgba(0,0,0,.18) 100%)}
</style>
</head>
<body>
<main class="canvas">
<div class="wall">

<section class="row">
  <article class="panel"><header class="panel-head"><h2 class="panel-title">We<br>keep you<br>connected</h2></header>
    <div class="panel-band"><p class="panel-copy">Trelvon Health Keeps Retirement<br>Communities Connected Through<br>Future-ready Telecom And Care Solutions</p></div>
    <div class="panel-photo" role="img" aria-label="Smiling woman using her smartphone at dusk" style="background:radial-gradient(ellipse 45% 30% at 45% 52%,#f0a040 0%,rgba(240,160,64,0) 100%),radial-gradient(ellipse 40% 25% at 55% 28%,#e9b48a,rgba(233,180,138,0) 100%),radial-gradient(ellipse 50% 25% at 40% 88%,#4d6d94,rgba(77,109,148,0) 100%),linear-gradient(160deg,#2b4668,#6e6a6a 45%,#8f6a3c 70%,#3b5878)"></div></article>
  <article class="panel"><header class="panel-head"><h2 class="panel-title">Our<br>journey &amp;<br>mission</h2></header>
    <div class="panel-band"><p class="panel-copy">20+ Years, 40,000+ Services,<br>From 2004 To Now.<br><b>Mission:</b> Bridging Distances,<br>Connecting Hearts</p></div>
    <div class="panel-photo" role="img" aria-label="Hand drawing a project timeline chart on a tablet" style="background:radial-gradient(ellipse 45% 25% at 55% 32%,#3b7da0,rgba(59,125,160,0) 100%),radial-gradient(ellipse 30% 18% at 65% 50%,#c07a9a,rgba(192,122,154,0) 100%),radial-gradient(ellipse 45% 18% at 70% 68%,#27394a,rgba(39,57,74,0) 100%),linear-gradient(170deg,#0e2436,#1b4561 50%,#0a1825)"></div></article>
  <article class="panel"><header class="panel-head"><h2 class="panel-title">People<br>centric<br>values</h2></header>
    <div class="panel-band"><p class="panel-copy">Dedication, Communication, Passion.<br>Personalized Local Support.</p></div>
    <div class="panel-photo" role="img" aria-label="Carer helping an older man use a tablet" style="background:radial-gradient(ellipse 35% 20% at 30% 30%,#d9b09a,rgba(217,176,154,0) 100%),radial-gradient(ellipse 35% 20% at 72% 45%,#e4c6b4,rgba(228,198,180,0) 100%),radial-gradient(ellipse 30% 22% at 35% 75%,#b9b9b9,rgba(185,185,185,0) 100%),linear-gradient(165deg,#5c7a3a,#8aa27a 25%,#7d8fa6 55%,#6b6b6b)"></div></article>
  <article class="panel"><header class="panel-head"><h2 class="panel-title">High speed<br>connectivity<br>fibre to<br>the home</h2></header>
    <div class="panel-band"><p class="panel-copy">Fast, Future-proof Internet.<br>Seamless Video Calls,<br>Streaming, Telehealth.</p></div>
    <div class="panel-photo" role="img" aria-label="Network switch with blue patch cables" style="background:radial-gradient(ellipse 25% 12% at 30% 45%,#8fd46a,rgba(143,212,106,0) 100%),radial-gradient(ellipse 50% 20% at 60% 20%,#3f7ae0,rgba(63,122,224,0) 100%),radial-gradient(ellipse 50% 25% at 55% 75%,#2a5fc0,rgba(42,95,192,0) 100%),linear-gradient(170deg,#7a86a0,#3b64a8 45%,#a68ca8 75%,#5d6f94)"></div></article>
  <article class="panel"><header class="panel-head"><h2 class="panel-title">Connectivity<br>everywhere<br>ethernet over<br>copper</h2></header>
    <div class="panel-band"><p class="panel-copy">Affordable Upgrades<br>Using Existing Wiring.<br>High-speed Broadband<br>Without Major Works.</p></div>
    <div class="panel-photo" role="img" aria-label="Ethernet plug with glowing fibre optic strands" style="background:radial-gradient(ellipse 30% 25% at 30% 12%,#9cc6ff,rgba(156,198,255,0) 100%),radial-gradient(ellipse 35% 20% at 55% 55%,#d9e4ea,rgba(217,228,234,0) 100%),radial-gradient(ellipse 25% 12% at 35% 50%,#e0b940,rgba(224,185,64,0) 100%),linear-gradient(160deg,#0a2070,#1e56c8 45%,#0a1a50 80%,#050c2a)"></div></article>
</section>

<section class="row">
  <article class="panel"><header class="panel-head"><h2 class="panel-title">Telephony<br>&amp; voice<br>services</h2></header>
    <div class="panel-band"><p class="panel-copy">Traditional &amp; Voip Lines.<br>In-house Call Systems For Internal<br>Communication.</p></div>
    <div class="panel-photo" role="img" aria-label="Desk IP phone beneath a cloud PBX diagram" style="background:radial-gradient(ellipse 30% 15% at 55% 38%,#e8dcd0,rgba(232,220,208,0) 100%),radial-gradient(ellipse 45% 25% at 55% 65%,#4a6a8c,rgba(74,106,140,0) 100%),radial-gradient(ellipse 60% 20% at 50% 92%,#7f98b4,rgba(127,152,180,0) 100%),linear-gradient(170deg,#0c1626,#1c3350 50%,#35557a)"></div></article>
  <article class="panel"><header class="panel-head"><h2 class="panel-title">Entertainment<br>&amp; media</h2></header>
    <div class="panel-band"><p class="panel-copy">Free-to-air Tv, Streamvale,<br>Dab+ Radio For Resident<br>Entertainment.</p></div>
    <div class="panel-photo" role="img" aria-label="Person facing a wall of glowing media screens" style="background:radial-gradient(ellipse 20% 10% at 60% 25%,#f07a4a,rgba(240,122,74,0) 100%),radial-gradient(ellipse 25% 12% at 40% 55%,#9ab8e0,rgba(154,184,224,0) 100%),radial-gradient(ellipse 18% 10% at 70% 72%,#f0c080,rgba(240,192,128,0) 100%),linear-gradient(160deg,#141d35,#2c2f4c 50%,#0a0f1e)"></div></article>
  <article class="panel"><header class="panel-head"><h2 class="panel-title">Safety &amp;<br>security cctv<br>surveillance</h2></header>
    <div class="panel-band"><p class="panel-copy">24/7 Surveillance,<br>Private Feeds,<br>Incident Tracking.</p></div>
    <div class="panel-photo" role="img" aria-label="Monitor showing CCTV camera feeds" style="background:radial-gradient(ellipse 50% 30% at 50% 35%,#6fb6d0,rgba(111,182,208,0) 100%),radial-gradient(ellipse 40% 8% at 50% 68%,#5ef0ff,rgba(94,240,255,0) 100%),linear-gradient(175deg,#0e0e0e 0%,#1d5e7a 12%,#2a86a6 45%,#0f3344 65%,#1a1a1a)"></div></article>
  <article class="panel"><header class="panel-head"><h2 class="panel-title">Secure access<br>control</h2></header>
    <div class="panel-band"><p class="panel-copy">Keypads, Swipe Cards,<br>Intercom Controlled Doors,<br>Privacy And Safety Ensured.</p></div>
    <div class="panel-photo" role="img" aria-label="Hand unlocking a smart door lock" style="background:radial-gradient(ellipse 12% 25% at 33% 55%,#3a3a3a,rgba(58,58,58,0) 100%),radial-gradient(ellipse 30% 15% at 70% 55%,#e8d8c4,rgba(232,216,196,0) 100%),linear-gradient(90deg,#e4e1dc,#f3f1ee 45%,#e6e0d6 70%,#d2cabe)"></div></article>
  <article class="panel"><header class="panel-head"><h2 class="panel-title">IP nurse call<br>&amp; intercom</h2></header>
    <div class="panel-band"><p class="panel-copy">Immediate Assistance<br>Via Pull Cords And<br>Emergency Intercoms.</p></div>
    <div class="panel-photo" role="img" aria-label="Hand pressing a nurse call handset" style="background:radial-gradient(ellipse 40% 15% at 45% 45%,#e6bca4,rgba(230,188,164,0) 100%),radial-gradient(ellipse 35% 20% at 40% 70%,#f4f4f4,rgba(244,244,244,0) 100%),radial-gradient(ellipse 15% 10% at 80% 45%,#f0a8b8,rgba(240,168,184,0) 100%),linear-gradient(160deg,#f2f2f2,#e4ded8 55%,#d8c0b0)"></div></article>
</section>

<section class="row">
  <article class="panel"><header class="panel-head"><h2 class="panel-title">Personal<br>emergency<br>devices</h2></header>
    <div class="panel-band"><p class="panel-copy">Fall Detection, Waterproof,<br>24/7 Monitoring.</p></div>
    <div class="panel-photo" role="img" aria-label="Finger pressing a red emergency stop button" style="background:radial-gradient(ellipse 45% 28% at 55% 32%,#f0c020,rgba(240,192,32,0) 100%),radial-gradient(ellipse 25% 16% at 55% 38%,#d83030,rgba(216,48,48,0) 100%),radial-gradient(ellipse 25% 25% at 85% 75%,#e0a890,rgba(224,168,144,0) 100%),linear-gradient(160deg,#555,#3a3a3a 55%,#2a2a2a)"></div></article>
  <article class="panel"><header class="panel-head"><h2 class="panel-title">Alvio<br>emergency<br>call system</h2></header>
    <div class="panel-band"><p class="panel-copy">4g Failsafe,<br>Real-time Alerts,<br>No Internet Dependency.</p></div>
    <div class="panel-photo" role="img" aria-label="Hands holding a small emergency call pendant" style="background:radial-gradient(ellipse 45% 18% at 50% 42%,#c89080,rgba(200,144,128,0) 100%),radial-gradient(ellipse 45% 25% at 50% 82%,#26344e,rgba(38,52,78,0) 100%),radial-gradient(ellipse 30% 20% at 85% 15%,#c8c8c8,rgba(200,200,200,0) 100%),linear-gradient(160deg,#22324e,#4a5468 50%,#1c2638)"></div></article>
  <article class="panel"><header class="panel-head"><h2 class="panel-title">Innovation &amp;<br>smart living</h2></header>
    <div class="panel-band"><p class="panel-copy">Iot Integration,smart Alarms,<br>Facial Recognition Entry.</p></div>
    <div class="panel-photo" role="img" aria-label="Finger touching a wall-mounted smart home panel" style="background:radial-gradient(ellipse 25% 22% at 30% 22%,#4a4e58,rgba(74,78,88,0) 100%),radial-gradient(ellipse 40% 25% at 55% 72%,#b8b0a8,rgba(184,176,168,0) 100%),linear-gradient(100deg,#5a606a,#7a7e84 35%,#d8dadc 60%,#eceeef)"></div></article>
  <article class="panel"><header class="panel-head"><h2 class="panel-title">Renewable<br>energy<br>solar power<br>integration</h2></header>
    <div class="panel-band"><p class="panel-copy">True Solar Via Fibre,<br>Efficient Energy Management.</p></div>
    <div class="panel-photo" role="img" aria-label="Aerial view of a large solar farm" style="background:radial-gradient(ellipse 40% 10% at 40% 82%,#4a9a5a,rgba(74,154,90,0) 100%),radial-gradient(ellipse 60% 15% at 50% 15%,#d8e0e8,rgba(216,224,232,0) 100%),linear-gradient(180deg,#b8c6d2,#7a8a7a 22%,#56687e 40%,#3d5068 80%,#46586e)"></div></article>
  <article class="panel"><header class="panel-head"><h2 class="panel-title">Safe power &amp;<br>battery<br>charging<br>Chargeguard</h2></header>
    <div class="panel-band"><p class="panel-copy">8-hour Auto Shutoff,<br>Fire Prevention,<br>Safe Lithium Charging.</p></div>
    <div class="panel-photo" role="img" aria-label="Glowing power symbol on a dark background" style="background:radial-gradient(circle at 50% 32%,#8ab4d8 0,#3d6d9c 12%,#1a3456 32%,#0b1628 60%,#060b16)"></div></article>
</section>

<section class="row">
  <article class="panel"><header class="panel-head"><h2 class="panel-title">Integrated<br>infrastructure<br>one-stop shop</h2></header>
    <div class="panel-band"><p class="panel-copy">Unified Delivery Of Internet, Tv, Voice,<br>Security, Solar, Emergency Services.</p></div>
    <div class="panel-photo" role="img" aria-label="Hand sketching a CRM cycle diagram on white" style="background:radial-gradient(ellipse 30% 20% at 65% 85%,#ecd0c0,rgba(236,208,192,0) 100%),radial-gradient(ellipse 40% 30% at 45% 35%,#e6e6e6,rgba(230,230,230,0) 100%),linear-gradient(180deg,#ffffff,#f6f6f6)"></div></article>
  <article class="panel"><header class="panel-head"><h2 class="panel-title">Resident<br>benefits</h2></header>
    <div class="panel-band"><p class="panel-copy">Better Connectivity,<br>Greater Independence,<br>Safety, Entertainment.</p></div>
    <div class="panel-photo" role="img" aria-label="Older man enjoying music on headphones" style="background:radial-gradient(ellipse 40% 28% at 45% 38%,#c89a84,rgba(200,154,132,0) 100%),radial-gradient(ellipse 30% 12% at 45% 14%,#e8e8e8,rgba(232,232,232,0) 100%),radial-gradient(ellipse 50% 25% at 50% 85%,#8a8c90,rgba(138,140,144,0) 100%),linear-gradient(160deg,#b8c2c8,#d4d8da 50%,#c8ccd0)"></div></article>
  <article class="panel"><header class="panel-head"><h2 class="panel-title">Operator &amp;<br>staff benefits</h2></header>
    <div class="panel-band"><p class="panel-copy">Cost Savings,<br>Operational Efficiency,<br>Real-time Data, Compliance</p></div>
    <div class="panel-photo" role="img" aria-label="Staff member monitoring data dashboards" style="background:radial-gradient(ellipse 50% 18% at 50% 12%,#3a6ec8,rgba(58,110,200,0) 100%),radial-gradient(ellipse 30% 15% at 30% 55%,#8ab0d8,rgba(138,176,216,0) 100%),radial-gradient(ellipse 25% 25% at 75% 60%,#c89a80,rgba(200,154,128,0) 100%),linear-gradient(170deg,#163a78,#22467e 40%,#1a1e28 80%)"></div></article>
  <article class="panel"><header class="panel-head"><h2 class="panel-title">Commitment<br>to innovation<br>&amp; quality</h2></header>
    <div class="panel-band"><p class="panel-copy">Trusted By Industry Leaders, Standards<br>Compliance, Long-term Partner</p></div>
    <div class="panel-photo" role="img" aria-label="Business handshake over a desk" style="background:radial-gradient(ellipse 25% 15% at 55% 50%,#d8a890,rgba(216,168,144,0) 100%),radial-gradient(ellipse 40% 22% at 35% 62%,#2a3248,rgba(42,50,72,0) 100%),radial-gradient(ellipse 40% 25% at 70% 25%,#c8c0b8,rgba(200,192,184,0) 100%),linear-gradient(160deg,#ece8e2,#b8b0a4 45%,#4a5060 65%,#d8d0c4)"></div></article>
  <article class="panel"><header class="panel-head"><h2 class="panel-title">Your smart<br>living partner</h2></header>
    <div class="panel-band"><p class="panel-copy">Connect With Trelvon<br>Health Today To Build<br>Smarter, Safer Communities.</p></div>
    <div class="panel-photo" role="img" aria-label="Hands on a laptop with floating contact icons" style="background:radial-gradient(ellipse 45% 15% at 60% 25%,#6ad8e8,rgba(106,216,232,0) 100%),radial-gradient(ellipse 45% 25% at 50% 72%,#1c7a94,rgba(28,122,148,0) 100%),radial-gradient(ellipse 25% 12% at 55% 48%,#9a7a70,rgba(154,122,112,0) 100%),linear-gradient(170deg,#0a2634,#14506a 50%,#06161e)"></div></article>
</section>

</div>
</main>
</body>
</html>
```